Re-vamp existing website :www.tallowmerefinch.com.au

We need a new website design for this website
www.tallowmerefinch.com.au.

"creating financial lightbulb moments"

Looking for something modern, corporate like this https://www.pebbleharbor.com.au

Imagery is important, showing really great images of what we do.

We want to keep the theme of:
Build Your Future
Invest in your Dreams
Grow You

We want a blog/opinion page on the website

Staying with our three logo colours throughout

Industry/Entity Type

Financial Service

Number of Pages Required

5+ page

```html
<!DOCTYPE html>
<html lang="en">
<head>
<meta charset="utf-8">
<title>Tallowmere Finch Financial Group</title>
<link rel="stylesheet" href="https://fonts.googleapis.com/css2?family=Montserrat:wght@400;500;600;700&family=Open+Sans:wght@400;600;700&display=swap">
<style>
:root{
  --sky:#00a3e8;
  --leaf:#8dc63f;
  --slate:#8a8d91;
  --ink:#1d1d1f;
  --text:#555a60;
  --muted:#8c9096;
  --topbar:#2b2f33;
  --footer:#262626;
  --footer-base:#1c1c1c;
  --line:#e6e8ea;
  --white:#ffffff;
}
*{box-sizing:border-box;margin:0;padding:0}
html,body{width:1200px;height:2628px;overflow:hidden;background:var(--white)}
body{font-family:"Open Sans",Arial,sans-serif;color:var(--text);position:relative}
.section{position:absolute;left:0;width:1200px}
.heading{font-family:"Montserrat",Arial,sans-serif;color:var(--ink)}

/* top bar */
.topbar{top:0;height:46px;background:var(--topbar);color:#d9dcdf;font-size:12px}
.topbar .contact{position:absolute;left:114px;top:0;height:46px;display:flex;align-items:center;gap:28px}
.topbar .contact span{display:flex;align-items:center;gap:8px}
.social{display:flex;gap:16px;align-items:center}
.topbar .social{position:absolute;right:114px;top:17px}
.dot{width:11px;height:11px;border-radius:50%;background:#d9dcdf;display:block}

/* header */
.header{top:46px;height:98px;background:var(--white)}
.header .nav-band{position:absolute;left:476px;top:0;width:724px;height:98px;background:var(--sky);clip-path:polygon(0 0,100% 0,100% 100%,42px 100%)}
.brand{position:absolute;left:114px;top:26px;display:flex;align-items:center;gap:12px}
.brand .mark{width:46px;height:46px;background:var(--sky)}
.brand .name{font-family:"Open Sans",Arial,sans-serif;font-weight:600;font-size:25px;color:var(--leaf);line-height:1}
.nav{position:absolute;left:556px;top:0;height:98px;display:flex;align-items:center;gap:36px;list-style:none}
.nav li{font-family:"Montserrat",Arial,sans-serif;font-size:13px;color:var(--white);letter-spacing:.3px}

/* hero */
.hero{top:144px;height:471px;background:linear-gradient(100deg,#4c5257 0%,#6b7074 35%,#8f8a86 60%,#5a5450 100%)}
.hero .title{position:absolute;left:114px;top:130px;font-size:51px;font-weight:600;line-height:53px;color:var(--white)}
.hero .lead{position:absolute;left:114px;top:250px;width:470px;font-size:15px;font-weight:600;line-height:26px;color:var(--white)}
.btn{position:absolute;top:329px;height:39px;font-family:"Montserrat",Arial,sans-serif;font-size:11px;font-weight:600;display:flex;align-items:center;justify-content:center}
.btn-primary{left:114px;width:122px;background:var(--sky);color:var(--white)}
.btn-light{left:252px;width:132px;background:var(--white);color:var(--ink)}
.slide-arrow{position:absolute;top:240px;width:30px;height:30px;border:1px solid var(--white);display:flex;align-items:center;justify-content:center}
.slide-arrow.prev{left:14px}.slide-arrow.next{right:14px}

/* journey */
.journey-title{top:672px;text-align:center;font-size:30px;font-weight:500}
.journey-copy{top:728px;left:255px;width:690px;text-align:center;font-size:11.5px;line-height:22px;color:#333}
.service{position:absolute;top:887px;width:302px;height:203px;overflow:hidden}
.service .photo{position:absolute;inset:0}
.service .caption{position:absolute;left:0;bottom:0;width:100%;height:48px;background:rgba(20,22,24,.82);display:flex;align-items:center}
.service .icon{width:48px;height:48px;background:var(--sky);display:flex;align-items:center;justify-content:center}
.service .label{padding-left:16px;font-family:"Montserrat",Arial,sans-serif;font-size:15px;font-weight:500;color:var(--white)}
.service.feature .caption{display:none}
.service.feature .side{position:absolute;left:0;top:0;width:48px;height:100%;background:var(--sky);display:flex;align-items:center;justify-content:center}
.service.feature .body{position:absolute;left:48px;top:0;width:254px;height:100%;background:rgba(20,22,24,.86);padding:44px 16px 0 16px}
.service.feature h3{font-family:"Montserrat",Arial,sans-serif;font-size:15px;font-weight:500;color:var(--sky);margin-bottom:12px}
.service.feature p{font-size:12.5px;line-height:22px;color:#e3e5e7}

/* partners */
.partners-title{top:1158px;text-align:center;font-size:28px;font-weight:500}
.pager{position:absolute;top:1152px;width:30px;height:30px;border:1px solid var(--line);display:flex;align-items:center;justify-content:center}
.partners{position:absolute;top:1235px;left:154px;width:890px;height:62px;display:flex;align-items:center;justify-content:space-between}
.partner{background:#c9ced3;border-radius:3px}

/* testimonial */
.testimonial{top:1349px;height:385px;background:linear-gradient(90deg,#f4efe7 0%,#e7e1d6 45%,#c9c6c0 70%,#9ea3a6 100%)}
.quote-box{position:absolute;left:215px;top:98px;width:435px;height:196px;border:1px solid #6f6f6f;background:rgba(255,255,255,.25)}
.quote-mark{position:absolute;left:34px;top:-16px;width:32px;height:32px;background:var(--sky);display:flex;align-items:center;justify-content:center}
.quote-text{position:absolute;right:36px;top:40px;width:360px;text-align:right;font-size:11.5px;line-height:22px;color:#3a3a3a}
.quote-name{position:absolute;right:36px;top:118px;font-family:"Montserrat",Arial,sans-serif;font-size:12px;color:var(--sky)}
.quote-role{position:absolute;right:36px;top:140px;font-size:11px;font-weight:600;color:#333}
.quote-nav{position:absolute;left:36px;top:126px;display:flex;gap:8px}
.quote-nav span{width:22px;height:22px;border:1px solid #bdbdbd;display:flex;align-items:center;justify-content:center}
.settings-tab{position:absolute;left:0;top:1451px;width:34px;height:38px;background:var(--sky);display:flex;align-items:center;justify-content:center}

/* blog */
.blog-title{top:1770px;text-align:center;font-size:28px;font-weight:500}
.post{position:absolute;top:1831px;width:302px;height:354px;border:1px solid #eeeff1;background:var(--white)}
.post .photo{height:163px}
.post .meta{margin:33px 16px 0;font-size:11px;color:#666}
.post h3{margin:6px 16px 0;font-family:"Open Sans",Arial,sans-serif;font-size:15px;font-weight:600;color:var(--sky)}
.post p{margin:14px 16px 0;font-size:11.5px;line-height:21px;color:var(--muted)}

/* footer */
.footer{top:2234px;height:329px;background:var(--footer);color:#9a9ea3}
.footer .brand-box{position:absolute;left:114px;top:62px;width:210px;height:48px;background:var(--white);display:flex;align-items:center;gap:8px;padding-left:8px}
.footer .brand-box .mark{width:30px;height:30px;background:var(--sky)}
.footer .brand-box .name{font-size:16px;font-weight:600;color:var(--leaf)}
.footer .about{position:absolute;left:114px;top:124px;width:210px;font-size:10.5px;line-height:21px}
.footer h4{position:absolute;top:54px;font-family:"Montserrat",Arial,sans-serif;font-size:19px;font-weight:400;color:#c4c7ca}
.footer ul{position:absolute;list-style:none;font-size:11.5px}
.footer .links{left:372px;top:124px}
.footer .links li{height:28px;display:flex;align-items:center;gap:8px}
.footer .links li::before{content:"";width:4px;height:4px;background:#777}
.news{position:absolute;left:605px;width:222px;font-size:11.5px;line-height:21px}
.news .date{font-size:10px;font-weight:600;color:var(--sky);margin-top:4px}
.news.one{top:122px;border-bottom:1px solid #3a3a3a;padding-bottom:10px}
.news.two{top:212px}
.footer .contact-list{left:852px;top:118px;width:240px}
.footer .contact-list li{display:flex;gap:14px;font-size:11.5px;line-height:21px;margin-bottom:14px}
.footer .social{position:absolute;left:852px;top:254px;gap:22px}
.footer .dot{background:#c4c7ca}
.footer-base{top:2563px;height:65px;background:var(--footer-base);font-size:11.5px;color:#8b8f94}
.footer-base .copy{position:absolute;left:114px;top:24px}
.footer-base .legal{position:absolute;right:128px;top:24px;display:flex;gap:26px}
</style>
</head>
<body>

<div class="section topbar">
  <div class="contact">
    <span><svg width="14" height="14" viewBox="0 0 24 24" fill="none" stroke="#d9dcdf" stroke-width="2"><path d="M5 3h4l2 5-3 2a12 12 0 0 0 6 6l2-3 5 2v4a2 2 0 0 1-2 2A17 17 0 0 1 3 5a2 2 0 0 1 2-2z"/></svg>Phone : 0400 555 019</span>
    <span><svg width="14" height="12" viewBox="0 0 24 18" fill="none" stroke="#d9dcdf" stroke-width="2"><rect x="1" y="1" width="22" height="16"/><path d="M1 1l11 9 11-9"/></svg>theteam@tallowmerefinch.com.au</span>
  </div>
  <div class="social"><i class="dot"></i><i class="dot"></i><i class="dot"></i><i class="dot"></i><i class="dot"></i></div>
</div>

<header class="section header">
  <div class="nav-band"></div>
  <div class="brand"><span class="mark"></span><span class="name">Tallowmere Finch</span></div>
  <ul class="nav"><li>HOME</li><li>ABOUT US</li><li>HOME LOANS</li><li>BUSINESS LENDING</li><li>CONTACT US</li></ul>
</header>

<section class="section hero" role="img" aria-label="Photo of two business colleagues smiling over a laptop in an office">
  <h1 class="heading title" style="color:var(--white)">We help business<br>innovate and grow</h1>
  <p class="lead">With over 10 years of experience helping businesses to find comprehensive solutions.</p>
  <span class="btn btn-primary">MEET EXPERTS</span>
  <span class="btn btn-light">CONTACT US</span>
  <span class="slide-arrow prev"><svg width="10" height="10" viewBox="0 0 10 10"><path d="M7 1L3 5l4 4" stroke="#fff" stroke-width="1.5" fill="none"/></svg></span>
  <span class="slide-arrow next"><svg width="10" height="10" viewBox="0 0 10 10"><path d="M3 1l4 4-4 4" stroke="#fff" stroke-width="1.5" fill="none"/></svg></span>
</section>

<h2 class="section heading journey-title">How your TMF journey works...</h2>
<p class="section journey-copy">Tallowmere Finch (TMF) is a leading Australian finance brokerage group dedicated in providing our clients with a range of financial solutions tailored to their individual requirements. We want our clients to be bold in chasing their financial dreams and we commit to provide a range of opportunities for them to do so. Tallowmere Finch aims to push the status quo by doing things differently. We want you to start thinking TMF and we can show you the steps to get you there. We know you have your vision of where you want to be, we will provide the guidance you might need in getting there.</p>

<div class="service feature" style="left:115px">
  <div class="photo" role="img" aria-label="Photo of a person working at a desk with screens" style="background:linear-gradient(135deg,#3a4a55,#1e262c)"></div>
  <div class="side"><svg width="20" height="18" viewBox="0 0 20 18" fill="none" stroke="#fff" stroke-width="1.5"><rect x="1" y="1" width="18" height="12"/><path d="M10 13v4M6 17h8M6 9l3-3 2 2 3-3"/></svg></div>
  <div class="body"><h3>About Business</h3><p>Business analytics (BA) is the practice of iterative, methodical exploration of an organization's data with emphasis on statistical analysis.</p></div>
</div>
<div class="service" style="left:441px">
  <div class="photo" role="img" aria-label="Photo of hands holding a smartphone above a laptop" style="background:linear-gradient(135deg,#e9e4dc,#b9b1a6 60%,#8d857b)"></div>
  <div class="caption"><span class="icon"><svg width="20" height="18" viewBox="0 0 20 18" fill="none" stroke="#fff" stroke-width="1.5"><path d="M10 1l9 4-9 4-9-4zM1 9l9 4 9-4M1 13l9 4 9-4"/></svg></span><span class="label">Advanced Analytics</span></div>
</div>
<div class="service" style="left:769px">
  <div class="photo" role="img" aria-label="Photo of a woman working on a laptop in a bright room" style="background:linear-gradient(135deg,#f2ece3,#d8c6b0 55%,#a8886a)"></div>
  <div class="caption"><span class="icon"><svg width="20" height="18" viewBox="0 0 20 18" fill="none" stroke="#fff" stroke-width="1.5"><rect x="1" y="1" width="18" height="12"/><path d="M10 13v4M6 17h8M5 10V7M9 10V4M13 10V6"/></svg></span><span class="label">Customer Insights</span></div>
</div>

<h2 class="section heading partners-title">Click Here to start your Journey!</h2>
<span class="pager" style="left:998px"><svg width="8" height="10" viewBox="0 0 8 10"><path d="M6 1L2 5l4 4" stroke="#bbb" stroke-width="1.5" fill="none"/></svg></span>
<span class="pager" style="left:1041px"><svg width="8" height="10" viewBox="0 0 8 10"><path d="M2 1l4 4-4 4" stroke="#bbb" stroke-width="1.5" fill="none"/></svg></span>
<div class="partners">
  <span class="partner" style="width:80px;height:16px"></span>
  <span class="partner" style="width:88px;height:28px"></span>
  <span class="partner" style="width:88px;height:28px"></span>
  <span class="partner" style="width:82px;height:24px"></span>
  <span class="partner" style="width:50px;height:54px"></span>
  <span class="partner" style="width:44px;height:54px"></span>
  <span class="partner" style="width:78px;height:40px"></span>
  <span class="partner" style="width:82px;height:20px"></span>
  <span class="partner" style="width:46px;height:58px"></span>
  <span class="partner" style="width:96px;height:22px"></span>
</div>

<section class="section testimonial" role="img" aria-label="Photo of a businessman leaning on a balcony looking at his phone above a city skyline">
  <div class="quote-box">
    <span class="quote-mark"><svg width="12" height="10" viewBox="0 0 12 10"><path d="M0 10V5L3 0h2L3 5h2v5zM7 10V5l3-5h2l-2 5h2v5z" fill="#fff"/></svg></span>
    <p class="quote-text">"Capitalise on low hanging fruit to identify a ballpark value added activity to beta test. Override the digital divide with additional clickthroughs from DevOps"</p>
    <div class="quote-nav"><span><svg width="6" height="8" viewBox="0 0 6 8"><path d="M5 1L1 4l4 3" stroke="#999" fill="none"/></svg></span><span><svg width="6" height="8" viewBox="0 0 6 8"><path d="M1 1l4 3-4 3" stroke="#999" fill="none"/></svg></span></div>
    <p class="quote-name">HAROLD PENWICK</p>
    <p class="quote-role">Chief Financial Officer</p>
  </div>
</section>
<span class="settings-tab"><svg width="14" height="14" viewBox="0 0 14 14"><circle cx="7" cy="7" r="4.5" fill="none" stroke="#fff" stroke-width="3" stroke-dasharray="2.4 1.2"/></svg></span>

<h2 class="section heading blog-title">From Blog</h2>
<article class="post" style="left:115px">
  <div class="photo" role="img" aria-label="Photo of a man on the phone working at a laptop" style="background:linear-gradient(135deg,#e8dcd2,#b08a7a 60%,#6c4c44)"></div>
  <p class="meta">by admin | January 23, 2017</p><h3>Retail banks wake up to digital</h3>
  <p>The great explorer of the truth, the master-builder of human happiness. No one rejects, dislikes, avoids pleasure itself, because it is pleasure, but because those ..</p>
</article>
<article class="post" style="left:441px">
  <div class="photo" role="img" aria-label="Photo of a man working at a computer in an office" style="background:linear-gradient(135deg,#8a8880,#5b5a54 55%,#3a3a36)"></div>
  <p class="meta">by admin | January 23, 2017</p><h3>Retail banks wake up to digital</h3>
  <p>The great explorer of the truth, the master-builder of human happiness. No one rejects, dislikes, avoids pleasure itself, because it is pleasure, but because those ..</p>
</article>
<article class="post" style="left:769px">
  <div class="photo" role="img" aria-label="Photo of a sailing boat on the sea at sunset" style="background:linear-gradient(180deg,#3d8fc4,#7fb8d8 45%,#e8c884 65%,#2a6a94)"></div>
  <p class="meta">by admin | January 23, 2017</p><h3>Retail banks wake up to digital</h3>
  <p>The great explorer of the truth, the master-builder of human happiness. No one rejects, dislikes, avoids pleasure itself, because it is pleasure, but because those ..</p>
</article>

<footer class="section footer">
  <div class="brand-box"><span class="mark"></span><span class="name">Tallowmere Finch</span></div>
  <p class="about">If you would like to enquire about starting your journey with Tallowmere Finch or simply wish to chat about your current position, please fill out our contact form and one of our team members will contact you within 24 hours.</p>
  <h4 style="left:360px">What We Do</h4>
  <ul class="links"><li>Organization</li><li>Customer Insights</li><li>Advanced Analytics</li><li>Performance</li><li>Sustainability</li><li>Business Growth</li></ul>
  <h4 style="left:605px">Latest News</h4>
  <div class="news one"><p>Seminar for improve your business profit &amp; loss</p><p class="date">January 31, 2018</p></div>
  <div class="news two"><p>Seminar for improve your business profit &amp; loss</p><p class="date">January 31, 2018</p></div>
  <h4 style="left:852px">Contact Us</h4>
  <ul class="contact-list">
    <li><svg width="12" height="14" viewBox="0 0 12 14"><path d="M6 13S1 8 1 5a5 5 0 0 1 10 0c0 3-5 8-5 8z" fill="#777"/></svg><span>Suite 4, Level 3, 21 Harbour Lane<br>Marrowby NSW 2090</span></li>
    <li><svg width="12" height="12" viewBox="0 0 24 24"><path d="M5 3h4l2 5-3 2a12 12 0 0 0 6 6l2-3 5 2v4a2 2 0 0 1-2 2A17 17 0 0 1 3 5a2 2 0 0 1 2-2z" fill="#777"/></svg><span>Phone: +0400 555 019</span></li>
    <li><svg width="12" height="12" viewBox="0 0 12 12"><path d="M1 6l10-5-3 10-2-4z" fill="#777"/></svg><span>theteam@tallowmerefinch.com.au</span></li>
  </ul>
  <div class="social"><i class="dot"></i><i class="dot"></i><i class="dot"></i><i class="dot"></i><i class="dot"></i></div>
</footer>
<div class="section footer-base">
  <p class="copy">Copyright © 2017 All Rights Reserved.</p>
  <div class="legal"><span>Legal</span><span>Sitemap</span><span>Privacy Policy</span><span>Terms &amp; Condition</span></div>
</div>

</body>
</html>
```